Social Media Graphics - Copperfield Loop

Create 6-7 individual social media graphics (square size) to encourage folks to join our online course, using either of the text below (only one set of text per graphic:

The Lantern Ridge Method
How to Create a 7-Figure Business From Scratch
Sign Up Today!

Or

The Lantern Ridge Method
Fast-track Your Way to a Multi-Million Business!
Sign Up Today!

For the color scheme of the graphics, use 1 or 2 colors in the color palette attached; or use any colors that look nice with their outfits; AVOID using red, white and blue altogether because it will look like an Independence Day (4th of July) graphic and we don’t want that; make sure the graphics appeal to both men and women

Make sure each graphic contains 1 of the 2 pics attached; and make sure one of the graphics is all TEXT only.

Target Market(s)

men and women looking to make more money

Industry/Entity Type

entrepreneurship

Requirements
Must have
• see the text document attached
Nice to have
• We are open to a nice color design; the color palette colors are not required, especially we don't want red, white and blue used together
Should not have
• AVOID using red, white and blue altogether because it will look like an Independence Day (4th of July) graphic and we dont want that

```html
<!DOCTYPE html>
<html lang="en">
<head>
<meta charset="utf-8">
<title>The Lantern Ridge Method – Sign Up Today</title>
<link rel="stylesheet" href="https://fonts.googleapis.com/css2?family=Poppins:wght@700;800;900&family=Great+Vibes&display=swap">
<style>
  :root {
    --canvas: #ffffff;
    --teal: #1e8fae;
    --teal-deep: #1c86a5;
    --cyan-glow: #22c6ec;
    --ghost-stroke: #2fe3f2;
    --type-light: #ffffff;
    --accent-pink: #ff3a6e;
    --navy: #0e2a44;
    --portrait-dark: #172634;
    --portrait-denim: #1f5a86;
  }
  * { box-sizing: border-box; margin: 0; padding: 0; }
  html, body {
    width: 1200px; height: 1200px; overflow: hidden;
    background: var(--canvas);
  }
  .graphic {
    position: relative; width: 1200px; height: 1200px;
    font-family: "Poppins", sans-serif;
  }
  .promo-panel {
    position: absolute; left: 131px; top: 131px;
    width: 951px; height: 854px; overflow: hidden;
    background:
      radial-gradient(ellipse 520px 420px at 300px 900px, var(--cyan-glow) 0%, rgba(34,198,236,0) 100%),
      linear-gradient(180deg, var(--teal) 0%, var(--teal-deep) 100%);
  }
  .title-ghost {
    position: absolute; left: 76px; top: 40px;
    font-weight: 900; font-size: 90px; line-height: 1; letter-spacing: 1px;
    color: transparent;
    -webkit-text-stroke: 2px var(--ghost-stroke);
    -webkit-mask-image: linear-gradient(180deg, #000 30%, rgba(0,0,0,0) 95%);
            mask-image: linear-gradient(180deg, #000 30%, rgba(0,0,0,0) 95%);
    white-space: nowrap;
  }
  .title-kicker {
    position: absolute; left: 52px; top: 190px;
    transform-origin: left top; transform: rotate(-90deg);
    font-weight: 800; font-size: 26px; letter-spacing: 1px;
    color: var(--type-light);
  }
  .title-main {
    position: absolute; left: 76px; top: 118px;
    font-weight: 900; font-size: 90px; line-height: 1; letter-spacing: 1px;
    color: var(--type-light); white-space: nowrap;
  }
  .title-script {
    position: absolute; left: 250px; top: 210px; z-index: 3;
    font-family: "Great Vibes", cursive;
    font-size: 200px; line-height: 1;
    color: var(--type-light);
  }
  .hosts-photo {
    position: absolute; left: 0; top: 320px;
    width: 631px; height: 534px; z-index: 2;
    border-radius: 260px 260px 0 0;
    background: linear-gradient(160deg, var(--portrait-dark) 0%, var(--portrait-denim) 100%);
  }
  .tagline {
    position: absolute; right: 70px; top: 408px;
    text-align: right;
    font-weight: 700; font-size: 54px; line-height: 62px;
    color: var(--type-light);
  }
  .cta {
    position: absolute; left: 0; top: 988px; width: 1200px;
    text-align: center;
    font-weight: 800; font-size: 80px; line-height: 1.1;
    color: var(--navy);
  }
  .cta-highlight { color: var(--accent-pink); }
</style>
</head>
<body>
  <main class="graphic">
    <section class="promo-panel">
      <div class="title-ghost" aria-hidden="true">LANTERN RIDGE</div>
      <div class="title-kicker">THE</div>
      <h1 class="title-main">LANTERN RIDGE</h1>
      <div class="title-script">Method</div>
      <div class="hosts-photo" role="img" aria-label="Photo of the two course hosts, a man in a black turtleneck with arms crossed and a woman in a denim blazer, both smiling"></div>
      <p class="tagline">How to<br>Create a<br>7-Figure<br>Business<br>From<br>Scratch</p>
    </section>
    <p class="cta"><span class="cta-highlight">SIGN UP</span> TODAY!</p>
  </main>
</body>
</html>
```